Reiki business card

Please see uploaded files. There is a word document on there explaining what is required and what the other uploaded files are for. I am after a soft, relaxing, warm welcoming feel to the card. Thank you.

Business

```html
<!DOCTYPE html>
<html lang="en">
<head>
<meta charset="utf-8">
<title>Reiki Business Card</title>
<link rel="stylesheet" href="https://fonts.googleapis.com/css2?family=Baloo+2:wght@400;500;700&display=swap">
<style>
  :root {
    --page-bg: #eef0f0;
    --teal-deep: #3c7f7c;
    --teal-mid: #4f9ea6;
    --teal-light: #7cc3d2;
    --mist: #b9dde6;
    --ink-white: #ffffff;
    --ink-soft: #eef7f8;
    --shadow: rgba(20, 60, 62, 0.35);
  }
  * { margin: 0; padding: 0; box-sizing: border-box; }
  html, body {
    width: 1200px; height: 800px; overflow: hidden;
    background: var(--page-bg);
    font-family: "Baloo 2", sans-serif;
  }
  .sheet {
    width: 1200px; height: 800px;
    display: flex; align-items: center; justify-content: center; gap: 40px;
  }
  .card {
    position: relative;
    width: 540px; height: 309px;
    border-radius: 4px;
    overflow: hidden;
    color: var(--ink-white);
    background:
      radial-gradient(ellipse 55% 60% at 82% 18%, var(--mist) 0%, rgba(185,221,230,0) 70%),
      radial-gradient(ellipse 50% 55% at 60% 75%, rgba(124,195,210,0.55) 0%, rgba(124,195,210,0) 70%),
      linear-gradient(100deg, var(--teal-deep) 0%, var(--teal-mid) 55%, var(--teal-light) 100%);
    box-shadow: 0 10px 28px rgba(40, 60, 60, 0.18);
  }
  .text-shadow { text-shadow: 3px 4px 6px var(--shadow); }

  /* Front */
  .front-illustration {
    position: absolute; left: 24px; top: 70px;
    width: 250px; height: 225px;
  }
  .front-title {
    position: absolute; left: 282px; top: 44px; width: 240px;
    text-align: center; font-weight: 700; text-transform: uppercase;
    font-size: 27px; line-height: 1.12; letter-spacing: 0.5px;
  }
  .front-title .title-main { font-size: 31px; letter-spacing: 1.5px; }
  .front-contact {
    position: absolute; left: 282px; top: 190px; width: 240px;
    text-align: center; font-weight: 500; font-size: 21px; line-height: 1.2;
    color: var(--ink-soft);
  }

  /* Back */
  .back-tagline {
    position: absolute; left: 150px; top: 52px; width: 360px;
    text-align: center; font-weight: 700; font-size: 25px; line-height: 1.15;
  }
  .back-contact {
    position: absolute; left: 40px; bottom: 40px; width: 470px;
    text-align: right; font-weight: 500; font-size: 18px; line-height: 1.6;
    color: var(--ink-soft);
  }
</style>
</head>
<body>
<main class="sheet">
  <section class="card card-front">
    <svg class="front-illustration" viewBox="0 0 250 225" role="img" aria-label="White silhouette illustration of a leafy tree sheltering a child and a dog">
      <defs>
        <radialGradient id="illustrationGlow" cx="45%" cy="45%" r="60%">
          <stop offset="0%" stop-color="#ffffff" stop-opacity="0.85"/>
          <stop offset="70%" stop-color="#ffffff" stop-opacity="0.45"/>
          <stop offset="100%" stop-color="#ffffff" stop-opacity="0"/>
        </radialGradient>
      </defs>
      <rect x="0" y="0" width="250" height="225" fill="url(#illustrationGlow)"/>
    </svg>
    <h1 class="front-title text-shadow">
      <span class="title-main">Reiki</span><br>
      For Little Ones<br>
      &amp; Animals
    </h1>
    <p class="front-contact text-shadow">Maren Holloway<br>0400 128 946</p>
  </section>

  <section class="card card-back">
    <p class="back-tagline text-shadow">Reiki - relaxes,<br>restores balance<br>&amp; promotes healing</p>
    <p class="back-contact text-shadow">hello@quietwillowreiki.com<br>quietwillowreiki.com</p>
  </section>
</main>
</body>
</html>
```